RW Personal Name/Business Card.

I need a double-sided name card with a logo/full design incorporating the "themes/concepts" of:
Neurology, wellness, Animals, Healing, Chiropractic, lifestyle, energy, creatvity & color on both sides of the card.
Information to include:
Name: Rosalind Webb
Mobile #: 0472 816 293
Email spinerwb@mailbrook.net

Possible use of "RW Health & Chiropractic"

Target Market(s)

People of all ages looking to improve their health & lifestyle.

Industry/Entity Type

Business

```html
<!DOCTYPE html>
<html lang="en">
<head>
<meta charset="utf-8">
<title>RW Health &amp; Chiropractic – Business Card</title>
<link href="https://fonts.googleapis.com/css2?family=Open+Sans:wght@400;600;700&display=swap" rel="stylesheet">
<style>
  :root {
    --stage: #e9e9ec;
    --card: #2a2d3f;
    --green: #6cbf3c;
    --white: #ffffff;
    --muted: #e4e6ee;
  }
  * { box-sizing: border-box; margin: 0; padding: 0; }
  html, body {
    width: 1200px; height: 676px; overflow: hidden;
    background: var(--stage);
    font-family: "Open Sans", sans-serif;
  }
  .stage {
    position: relative; width: 1200px; height: 676px;
  }
  .card {
    position: absolute; top: 190px;
    width: 520px; height: 297px;
    background: var(--card);
    color: var(--white);
    overflow: hidden;
    box-shadow: 0 6px 18px rgba(0,0,0,0.18);
  }
  .card--front { left: 50px; }
  .card--back { left: 630px; }

  .brand-title {
    font-weight: 400;
    font-size: 31px;
    letter-spacing: 0.2px;
    white-space: nowrap;
  }
  .brand-title .amp { color: var(--green); }

  .card--front .brand-title {
    position: absolute; left: 30px; top: 28px;
  }
  .contact {
    position: absolute; right: 30px; top: 142px;
    text-align: right;
  }
  .contact__name {
    color: var(--green);
    font-weight: 700;
    font-size: 17px;
    margin-bottom: 6px;
  }
  .contact__line {
    display: flex; justify-content: flex-end; align-items: center;
    gap: 7px;
    font-size: 12.5px;
    line-height: 19px;
    color: var(--muted);
  }
  .contact__icon { width: 12px; height: 12px; flex: none; }
  .front-band {
    position: absolute; left: 0; right: 0; bottom: 0;
    height: 16px; background: var(--green);
  }

  .card--back .brand-title {
    position: absolute; left: 26px; top: 150px;
    color: var(--green);
  }
  .card--back .brand-title .amp { color: var(--white); }
  .themes {
    position: absolute; left: 26px; top: 196px;
    font-size: 13.5px; line-height: 21px;
    color: var(--muted);
  }
</style>
</head>
<body>
<main class="stage">
  <section class="card card--front" aria-label="Business card front">
    <h1 class="brand-title">RW Health <span class="amp">&amp;</span> Chiropractic</h1>
    <div class="contact">
      <p class="contact__name">Rosalind Webb</p>
      <p class="contact__line">0472 816 293
        <svg class="contact__icon" viewBox="0 0 12 12" aria-hidden="true"><rect x="3" y="0.5" width="6" height="11" rx="1" fill="none" stroke="#6cbf3c" stroke-width="1.2"/><circle cx="6" cy="9.5" r="0.8" fill="#6cbf3c"/></svg>
      </p>
      <p class="contact__line">spinerwb@mailbrook.net
        <svg class="contact__icon" viewBox="0 0 12 12" aria-hidden="true"><rect x="0.6" y="2" width="10.8" height="8" fill="#6cbf3c"/><path d="M0.6 2 L6 6.5 L11.4 2" fill="none" stroke="#2a2d3f" stroke-width="1"/></svg>
      </p>
      <p class="contact__line">www.yourwebsite.com
        <svg class="contact__icon" viewBox="0 0 12 12" aria-hidden="true"><circle cx="6" cy="6" r="5.4" fill="#6cbf3c"/><ellipse cx="6" cy="6" rx="2.3" ry="5.4" fill="none" stroke="#2a2d3f" stroke-width="0.9"/><line x1="0.6" y1="6" x2="11.4" y2="6" stroke="#2a2d3f" stroke-width="0.9"/></svg>
      </p>
    </div>
    <div class="front-band"></div>
  </section>

  <section class="card card--back" aria-label="Business card back">
    <h2 class="brand-title">RW Health <span class="amp">&amp;</span> Chiropractic</h2>
    <p class="themes">
      Neurology | Wellness | Animals | Healing | Chiropractic<br>
      Lifestyle | Energy | Creatvity &amp; color on both sides.
    </p>
  </section>
</main>
</body>
</html>
```